Lift Her Summit - Marketing Graphic Needed

Non-profit needs a full page and header size graphic for our 2023 Lift Her Summit.

The theme this year is: Unrestrained
Date: January 27, 2023
Location: Harborlight Stays Meeting Hall | San Marcos, TX
Focus (not to be included on flyer): identifying what's holding us back; moving forward; practice makes progress; creating new paradigms; dispelling self-sabotage; clarifying goals; how to kick butt and play to win; being true to your self; building self-confidence; working less to get more.

Target Market(s)

Women in the design and construction industry (architects, engineers, project managers, project Owners, attorneys)

Industry/Entity Type

Design and Construction

Requirements
Must have
• Title of Forum, Theme, date, location, Q-BraTM logo and Lift Her logo
Nice to have
• a graphic that exemplifies the theme: "Unrestrained"

```html
<!DOCTYPE html>
<html lang="en">
<head>
<meta charset="utf-8">
<title>Lift Her Summit 2023 – Unrestrained</title>
<link rel="stylesheet" href="https://fonts.googleapis.com/css2?family=Abril+Fatface&family=Anton&family=Encode+Sans+Condensed:wght@700&display=swap">
<style>
  :root {
    --paper: #ffffff;
    --theme-blue: #3c3f96;
    --title-ink: #2e2a6e;
    --summit-pink: #e9218d;
    --ink-dark: #333333;
    --venue-green: #a6c94a;
    --panel-grey: #d1d2d4;
    --figure-dark: #3a3a3a;
    --figure-light: #8a8a8a;
  }
  html, body {
    margin: 0;
    padding: 0;
    overflow: hidden;
    background: var(--paper);
  }
  .header-banner {
    display: block;
    width: 1200px;
    height: 300px;
    background: var(--paper);
  }
  .summit-band { fill: var(--summit-pink); }
  .summit-title {
    font-family: "Abril Fatface", Georgia, serif;
    font-size: 27px;
    fill: var(--title-ink);
  }
  .theme-word {
    font-family: "Anton", Impact, sans-serif;
    font-size: 110px;
    fill: var(--theme-blue);
  }
  .event-date {
    font-family: "Encode Sans Condensed", "Arial Narrow", sans-serif;
    font-weight: 700;
    font-size: 48px;
    fill: var(--ink-dark);
  }
  .venue-pill { fill: var(--venue-green); }
  .venue-text {
    font-family: "Encode Sans Condensed", "Arial Narrow", sans-serif;
    font-weight: 700;
    font-size: 32px;
    fill: var(--ink-dark);
  }
  .partner-panel { fill: var(--panel-grey); }
  .partner-name {
    font-family: "Encode Sans Condensed", "Arial Narrow", sans-serif;
    font-weight: 700;
    font-size: 46px;
    fill: var(--ink-dark);
  }
</style>
</head>
<body>
<svg class="header-banner" viewBox="0 0 1200 300" xmlns="http://www.w3.org/2000/svg">
  <defs>
    <linearGradient id="figure-tone" x1="0" y1="0" x2="0" y2="1">
      <stop offset="0" stop-color="var(--figure-dark)"/>
      <stop offset="1" stop-color="var(--figure-light)" stop-opacity="0.35"/>
    </linearGradient>
  </defs>

  <rect class="hero-figure" x="84" y="10" width="128" height="230" rx="58" fill="url(#figure-tone)"
        role="img" aria-label="Line illustration of a woman with long flowing hair, seen from behind"/>

  <rect class="summit-band" x="256" y="38" width="490" height="32"/>
  <text class="summit-title" x="501" y="64" text-anchor="middle" textLength="408" lengthAdjust="spacingAndGlyphs">Lift Her Summit 2023</text>

  <text class="theme-word" x="210" y="166" textLength="584" lengthAdjust="spacingAndGlyphs">Unrestrained</text>

  <text class="event-date" x="264" y="219" textLength="478" lengthAdjust="spacingAndGlyphs">Date: January 27, 2023</text>

  <rect class="venue-pill" x="74" y="238" width="764" height="58" rx="29"/>
  <text class="venue-text" x="457" y="279" text-anchor="middle" textLength="658" lengthAdjust="spacingAndGlyphs">Harborlight Stays Meeting Hall | San Marcos, TX</text>

  <polygon class="partner-panel" points="836,170 880,40 1156,40 1156,298 880,298"/>
  <text class="partner-name" x="1012" y="184" text-anchor="middle">Q-BraTM</text>
</svg>
</body>
</html>
```